Harborlight Capital Estates business card

We are a real estate advisory and investment company. We are specialized in assisting high networth individuals to invest in real estate overseas. We deliver a very personalized service, anticipating all the potential challenges an investor can face, and making it easy and safe for them. We also co-invest with our clients, assuring them that each project will be looked after as it is our own, and at the same time giving them the extra booth on confidence to invest.

We need a business card design. The business card must have a very premium, high-end look, reflecting principles like "commitment", "trust" and "timeless (but contemporary)". We look for long term relationships with our clients, and we grow with their referrals. We are all about conquering the confidence of the clients by always delivering above the expectations performance.

Target Market(s)

High net worth individuals.

Industry/Entity Type

Real Estate

Contact Information for Business Card

Please consider places on the business card for:

Name
Function (bellow name in smaller size text)

Mobile phone
E-mail
Skype ID
WeChat ID

Adress (3 lines)

Also include the following locations references:
PORTUGAL * DUBAI * HONG KONG

Website: www.hcestates-example.com

Requirements
Must have
• Company Logo

```html
<!DOCTYPE html>
<html lang="en">
<head>
<meta charset="utf-8">
<title>Harborlight Capital Estates – Business Card</title>
<link rel="stylesheet" href="https://fonts.googleapis.com/css2?family=Tinos:wght@400;700&family=Oswald:wght@600&display=swap">
<style>
  :root {
    --backdrop: #2a2a2c;
    --brand-blue: #2aa7e1;
    --brand-blue-deep: #1b8fc6;
    --card-white: #ffffff;
    --ink-grey: #6b6b6b;
    --ink-white: #ffffff;
  }
  * { margin: 0; padding: 0; box-sizing: border-box; }
  html, body {
    width: 1200px; height: 750px; overflow: hidden;
    background: var(--backdrop);
  }
  .stage {
    width: 1200px; height: 750px;
    display: flex; align-items: center; justify-content: center; gap: 44px;
  }
  .card {
    position: relative;
    width: 540px; height: 310px;
    border-radius: 18px;
    overflow: hidden;
    font-family: "Tinos", "Times New Roman", serif;
  }
  /* Back side */
  .card--back { background: var(--brand-blue); color: var(--ink-white); }
  .contact {
    position: absolute; top: 40px; right: 40px; width: 230px;
    font-size: 13px; line-height: 1.25;
  }
  .contact__address { margin-bottom: 8px; }
  .contact__list { list-style: none; }
  .contact__item { display: flex; align-items: center; gap: 8px; height: 19px; font-size: 14px; }
  .contact__icon { width: 13px; height: 13px; flex: none; }
  .brand-block {
    position: absolute; left: 36px; bottom: 40px;
  }
  .brand-block__name {
    font-size: 25px; font-weight: 700; letter-spacing: 0.5px; color: var(--ink-white);
    padding-bottom: 6px; border-bottom: 1px solid var(--ink-white);
  }
  .brand-block__locations {
    margin-top: 6px;
    font-family: "Oswald", "Arial Narrow", sans-serif;
    font-weight: 600; font-size: 15px; letter-spacing: 0.6px;
  }
  /* Front side */
  .card--front { background: var(--card-white); }
  .front-brand {
    position: absolute; right: 36px; top: 120px;
    font-size: 23px; font-weight: 700; color: var(--brand-blue);
    padding-bottom: 5px; border-bottom: 1px solid var(--ink-grey);
  }
  .holder { position: absolute; left: 36px; bottom: 40px; }
  .holder__name {
    font-size: 22px; font-weight: 700; color: var(--brand-blue); letter-spacing: 0.3px;
  }
  .holder__role { font-size: 19px; color: var(--ink-grey); }
</style>
</head>
<body>
<main class="stage">
  <section class="card card--back" aria-label="Card back">
    <div class="contact">
      <p class="contact__address">N. 8 Quayside Row,<br>Suite 210, Marlow Bay,<br>WA 50123</p>
      <ul class="contact__list">
        <li class="contact__item">
          <svg class="contact__icon" viewBox="0 0 16 16"><rect x="1" y="1" width="14" height="14" rx="3" fill="none" stroke="#fff"/><path d="M5 4h2l1 2-1 1c.5 1 1 1.5 2 2l1-1 2 1v2c-4 0-7-3-7-7z" fill="#fff"/></svg>
          <span>555.010.2030</span>
        </li>
        <li class="contact__item">
          <svg class="contact__icon" viewBox="0 0 16 16"><rect x="1" y="1" width="14" height="14" rx="3" fill="none" stroke="#fff"/><rect x="4" y="5" width="8" height="6" fill="none" stroke="#fff"/><path d="M4 5l4 3 4-3" fill="none" stroke="#fff"/></svg>
          <span>info@hcestates-example.com</span>
        </li>
        <li class="contact__item">
          <svg class="contact__icon" viewBox="0 0 16 16"><circle cx="8" cy="8" r="6.5" fill="none" stroke="#fff"/><ellipse cx="8" cy="8" rx="2.8" ry="6.5" fill="none" stroke="#fff"/><path d="M1.5 8h13" stroke="#fff"/></svg>
          <span>www.hcestates-example.com</span>
        </li>
        <li class="contact__item">
          <svg class="contact__icon" viewBox="0 0 16 16"><circle cx="8" cy="8" r="6.5" fill="none" stroke="#fff"/></svg>
          <span>/hcEstates</span>
        </li>
        <li class="contact__item">
          <svg class="contact__icon" viewBox="0 0 16 16"><circle cx="8" cy="8" r="6.5" fill="#fff"/></svg>
          <span>/hcEstates</span>
        </li>
      </ul>
    </div>
    <div class="brand-block">
      <p class="brand-block__name">Harborlight Capital Estates</p>
      <p class="brand-block__locations">PORTUGAL • DUBAI • HONG KONG</p>
    </div>
  </section>

  <section class="card card--front" aria-label="Card front">
    <p class="front-brand">Harborlight Capital Estates</p>
    <div class="holder">
      <p class="holder__name">DANIEL MERCER</p>
      <p class="holder__role">President</p>
    </div>
  </section>
</main>
</body>
</html>
```